Updated Stationary needed using new logo for Hair Tissue Mineral Analysis Company

Simple stationary design needed using new logo!
1. 8.5" x 11" Letterhead with company information listed below
2. 8.5" x 11" Design with Footer only with logo and information for print materials
3. 5.5" x 8.5" letterhead design
4. 4.125" x 9.5" Business envelope (#10 envelope) with address
5. 4.125" x 9.5" Business envelope with clear window (#10 envelope) with address
6. 6.5" x 9.5" envelope (6 3/4 Booklet envelope) with address
7. 10" x 13" Open End envelope
Address:
4817 N. Corwin Street
Phoenix, AZ 85021
Phone:
(602)-417-3926
Website:
www.pexumor.com
Email:
information@pexumor.com
Updates
Need extra days to review
Focused on completing other projects first
Look and feel
Each slider illustrates characteristics of the customer's brand and the style your logo design should communicate.

```html
<!DOCTYPE html>
<html lang="en">
<head>
<meta charset="utf-8">
<title>Pexumor Labs Stationery</title>
<link href="https://fonts.googleapis.com/css2?family=Arimo:wght@400;700&display=swap" rel="stylesheet">
<style>
  :root{
    --backdrop:#bbbbbb;
    --paper:#ffffff;
    --brand-blue:#2a5a9f;
    --accent-orange:#f28a30;
    --light-blue:#5b84c8;
    --flap-navy:#0b1a3a;
    --ink:#1a1a1a;
  }
  html,body{margin:0;padding:0;width:1200px;height:1200px;overflow:hidden;background:var(--backdrop);}
  .sheet-set{display:block;width:1200px;height:1200px;font-family:"Arimo",Arial,sans-serif;}
  .paper{fill:var(--paper);}
  .paper-edge{fill:#a9a9a9;}
  .brand-name{fill:var(--brand-blue);font-weight:700;letter-spacing:1px;}
  .brand-mark{fill:var(--accent-orange);}
  .stripe-solid{fill:var(--brand-blue);}
  .tick-orange{fill:var(--accent-orange);}
  .tick-blue{fill:var(--light-blue);}
  .contact{fill:var(--ink);font-weight:400;}
  .icon{fill:var(--accent-orange);}
  .address-blue{fill:var(--brand-blue);font-weight:400;}
  .flap{fill:var(--brand-blue);}
  .side-flap{fill:var(--flap-navy);}
</style>
</head>
<body>
<svg class="sheet-set" viewBox="0 0 1932 1932" xmlns="http://www.w3.org/2000/svg">
  <defs>
    <g id="ticks">
      <polygon class="tick-orange" points="8,0 18,0 10,17 0,17"/>
      <polygon class="tick-orange" points="22,0 32,0 24,17 14,17"/>
      <polygon class="tick-blue" points="36,0 46,0 38,17 28,17"/>
      <polygon class="tick-blue" points="50,0 60,0 52,17 42,17"/>
    </g>
    <g id="icon-phone">
      <path class="icon" d="M0 4 Q6 -1 12 4 L10 6 L8 4 L4 4 L2 6 Z M2 7 L10 7 L11 11 L1 11 Z"/>
    </g>
    <g id="icon-send">
      <polygon class="icon" points="0,6 12,0 7,12 5,7"/>
    </g>
    <g id="icon-globe">
      <circle class="icon" cx="6" cy="6" r="6"/>
      <circle cx="6" cy="6" r="3" fill="#fff" opacity=".6"/>
    </g>
  </defs>

  <!-- Letterhead with footer -->
  <g class="letterhead-footer">
    <rect class="paper-edge" x="228" y="97" width="771" height="997"/>
    <rect class="paper" x="228" y="96" width="770" height="996"/>
    <rect class="brand-mark" x="646" y="944" width="28" height="28"/>
    <text class="brand-name" x="975" y="970" font-size="36" text-anchor="end">PEXUMOR LABS</text>
    <use href="#ticks" transform="translate(475,997)"/>
    <polygon class="stripe-solid" points="539,997 998,997 998,1014 531,1014"/>
    <use href="#icon-phone" transform="translate(252,1046)"/>
    <text class="contact" x="268" y="1057" font-size="14">(602)-417-3926</text>
    <use href="#icon-send" transform="translate(380,1045)"/>
    <text class="contact" x="396" y="1056" font-size="14">information@pexumor.com</text>
    <use href="#icon-globe" transform="translate(568,1045)"/>
    <text class="contact" x="585" y="1055" font-size="14">www.pexumor.com</text>
    <text class="contact" x="975" y="1046" font-size="14" text-anchor="end">4817 N. Corwin Street</text>
    <text class="contact" x="975" y="1065" font-size="14" text-anchor="end">Phoenix, AZ 85021</text>
  </g>

  <!-- Half-size letterhead -->
  <g class="letterhead-half">
    <rect class="paper-edge" x="1055" y="92" width="649" height="1003"/>
    <rect class="paper" x="1055" y="91" width="648" height="1003"/>
    <rect class="brand-mark" x="1078" y="121" width="28" height="28"/>
    <text class="brand-name" x="1116" y="147" font-size="36">PEXUMOR LABS</text>
    <use href="#ticks" transform="translate(1235,981) scale(1.35)"/>
    <polygon class="stripe-solid" points="1321,981 1703,981 1703,1004 1311,1004"/>
    <use href="#icon-phone" transform="translate(1106,1026) scale(1.3)"/>
    <text class="contact" x="1128" y="1040" font-size="18">(602)-417-3926</text>
    <use href="#icon-send" transform="translate(1272,1026) scale(1.2)"/>
    <text class="contact" x="1293" y="1039" font-size="18">information@pexumor.com</text>
    <use href="#icon-globe" transform="translate(1518,1026) scale(1.2)"/>
    <text class="contact" x="1539" y="1038" font-size="18">www.pexumor.com</text>
    <text class="contact" x="1680" y="1066" font-size="18" text-anchor="end">4817 N. Corwin Street Phoenix, AZ 85021</text>
  </g>

  <!-- Open end envelope, unfolded -->
  <g class="envelope-large">
    <path class="flap" d="M114 1150 L700 1150 Q708 1150 711 1160 L737 1256 L77 1256 L103 1160 Q106 1150 114 1150 Z"/>
    <path class="flap" d="M77 1540 L737 1540 L711 1772 Q709 1785 697 1785 L117 1785 Q105 1785 103 1772 Z"/>
    <path class="side-flap" d="M77 1255 L48 1272 Q41 1277 41 1286 L41 1510 Q41 1519 48 1523 L77 1541 Z"/>
    <path class="side-flap" d="M737 1255 L764 1270 Q771 1275 771 1284 L771 1512 Q771 1521 764 1525 L737 1541 Z"/>
    <rect class="paper" x="77" y="1255" width="660" height="286"/>
    <text class="address-blue" x="96" y="1488" font-size="15">4817 N. Corwin Street</text>
    <text class="address-blue" x="96" y="1506" font-size="15">Phoenix, AZ 85021</text>
    <use href="#ticks" transform="translate(316,1487) scale(0.765)"/>
    <polygon class="stripe-solid" points="365,1487 716,1487 716,1500 359,1500"/>
  </g>

  <!-- Booklet envelope, unfolded -->
  <g class="envelope-booklet">
    <path class="flap" d="M870 1189 L1234 1189 Q1241 1189 1242 1197 L1258 1312 L845 1312 L861 1197 Q862 1189 870 1189 Z"/>
    <path class="flap" d="M845 1594 L1258 1594 L1242 1774 Q1241 1785 1231 1785 L872 1785 Q862 1785 861 1774 Z"/>
    <path class="side-flap" d="M845 1311 L828 1321 Q822 1325 822 1333 L822 1575 Q822 1582 828 1586 L845 1595 Z"/>
    <path class="side-flap" d="M1258 1311 L1275 1321 Q1281 1325 1281 1333 L1281 1575 Q1281 1582 1275 1586 L1258 1595 Z"/>
    <rect class="paper" x="845" y="1311" width="413" height="284"/>
    <text class="address-blue" x="858" y="1555" font-size="9">4817 N. Corwin Street</text>
    <text class="address-blue" x="858" y="1566" font-size="9">Phoenix, AZ 85021</text>
    <use href="#ticks" transform="translate(995,1555) scale(0.47)"/>
    <polygon class="stripe-solid" points="1025,1555 1245,1555 1245,1563 1021,1563"/>
  </g>

  <!-- #10 business envelope -->
  <g class="envelope-business">
    <rect class="paper-edge" x="1333" y="1337" width="551" height="238"/>
    <rect class="paper" x="1333" y="1336" width="550" height="238"/>
    <text class="address-blue" x="1350" y="1529" font-size="12">4817 N. Corwin Street</text>
    <text class="address-blue" x="1350" y="1544" font-size="12">Phoenix, AZ 85021</text>
    <use href="#ticks" transform="translate(1533,1529) scale(0.59)"/>
    <polygon class="stripe-solid" points="1571,1529 1866,1529 1866,1539 1566,1539"/>
  </g>
</svg>
</body>
</html>
```